we need a business card design for a professional painting business. This company has been up and going for about ten years. However it needs an new logo. we want this business card to be modern eye catching and easy to read. I currently have been looking for VP logos but can not find one that suits our needs. This Design should be Our start to a new beginning.
Industry/Entity Type
Painting
Contact Information for Business Card
Varesko Painting Inc.
Licensed & Insured
Tomas Varesko
Phone(631)384-4562
Fax (555) 846-3021
E-mail vareskopaintinginc@mailorbit.test
Requirements
Must have
- a new logo with  VP and i would like it to be in black and white.
i would also like the front to be a solid black with the logo only and then the back to have the information.

```html
<!DOCTYPE html>
<html lang="en">
<head>
<meta charset="utf-8">
<title>Varesko Painting Inc. – Business Card</title>
<link href="https://fonts.googleapis.com/css2?family=Roboto+Condensed:wght@700&family=Didact+Gothic&family=Arimo&family=Questrial&display=swap" rel="stylesheet">
<style>
  :root {
    --page-bg: #e6e6e6;
    --card-black: #050505;
    --card-white: #ffffff;
    --mark-dark: #231f20;
    --ink: #1a1a1a;
    --ink-soft: #2b2b2b;
    --band-grey: #bcbec0;
    --accent-red: #e0201f;
    --white: #ffffff;
  }
  * { box-sizing: border-box; margin: 0; padding: 0; }
  html, body {
    width: 1200px; height: 1200px; overflow: hidden;
    background: var(--page-bg);
  }
  .sheet {
    width: 1200px; height: 1200px;
    display: flex; flex-direction: column; align-items: center; justify-content: center;
    gap: 52px;
  }
  .card {
    position: relative;
    width: 900px; height: 514px;
    overflow: hidden;
    box-shadow: 0 6px 18px rgba(0,0,0,0.18);
  }

  /* Front */
  .card--front {
    background: var(--card-black);
    display: flex; flex-direction: column; align-items: center; justify-content: center;
    gap: 26px;
  }
  .front-mark {
    width: 150px; height: 150px;
    background: var(--mark-dark);
    border: 2px solid #3a3a3a;
  }
  .front-name {
    font-family: "Didact Gothic", sans-serif;
    font-size: 30px; letter-spacing: 1px;
    color: var(--white);
  }

  /* Back */
  .card--back { background: var(--card-white); }
  .back-mark {
    position: absolute; left: 70px; top: 36px;
    width: 124px; height: 124px;
    background: var(--mark-dark);
  }
  .company {
    position: absolute; left: 222px; top: 44px;
    font-family: "Roboto Condensed", sans-serif;
    font-weight: 700; font-size: 50px; line-height: 1;
    color: var(--ink); letter-spacing: 0.5px;
  }
  .credential {
    position: absolute; left: 222px; top: 102px;
    font-family: "Arimo", sans-serif; font-weight: 400;
    font-size: 30px; line-height: 1;
    color: var(--accent-red); letter-spacing: 1.5px;
    -webkit-text-stroke: 0.6px var(--accent-red);
  }
  .band-top {
    position: absolute; left: 0; right: 0; top: 172px; height: 38px;
    background: var(--band-grey);
  }
  .band-name {
    position: absolute; left: 430px; right: 0; top: 278px; height: 50px;
    background: var(--band-grey);
    display: flex; align-items: center; justify-content: flex-end;
    padding-right: 80px;
  }
  .person {
    font-family: "Questrial", sans-serif; font-weight: 400;
    font-size: 32px; line-height: 1; color: var(--ink-soft); letter-spacing: 1px;
    -webkit-text-stroke: 0.7px var(--ink-soft);
  }
  .contact {
    position: absolute; left: 470px; top: 360px;
    list-style: none;
    font-family: "Didact Gothic", sans-serif;
    font-size: 28px; line-height: 1; color: var(--ink);
    letter-spacing: 1px;
  }
  .contact li { margin-bottom: 20px; }
  .contact .email {
    font-family: "Arimo", sans-serif; font-size: 25px; letter-spacing: 0;
  }
</style>
</head>
<body>
  <main class="sheet">
    <section class="card card--front" aria-label="Card front">
      <div class="front-mark"></div>
      <p class="front-name">VARESKO PAINTING INC.</p>
    </section>

    <section class="card card--back" aria-label="Card back">
      <div class="back-mark"></div>
      <h1 class="company">VARESKO PAINTING INC</h1>
      <p class="credential">LICENSED AND INSURED</p>
      <div class="band-top"></div>
      <div class="band-name">
        <p class="person">Tomas Varesko</p>
      </div>
      <ul class="contact">
        <li>555.217.9083</li>
        <li>FAX 555.846.3021</li>
        <li class="email">vareskopaintinginc@mailorbit.test</li>
      </ul>
    </section>
  </main>
</body>
</html>
```